Webdesign mit Software und IT Schwerpunkt
Zielgruppe
kleine und mittelständische Untrenehmen
Aufgabenstellung
Software-Service-Gesellschaft, spezialisiert auf Entwicklung und Betrieb von gewerblichen Webseiten mit selbstentwickeltem Service-Tool

```html
<!DOCTYPE html>
<html lang="de">
<head>
<meta charset="utf-8">
<title>Webhaus – Wir halten Sie im Web</title>
<link href="https://fonts.googleapis.com/css2?family=Open+Sans:wght@400;600;700&family=Arimo:wght@400;700&display=swap" rel="stylesheet">
<style>
:root{
  --bg-dark:#2b2b2b;
  --page:#ffffff;
  --orange:#f47f20;
  --orange-band:rgba(214,110,30,.75);
  --gray-band:rgba(120,120,120,.6);
  --nav-active:#3e3e3e;
  --banner:#4a86ad;
  --text:#333333;
  --muted:#666666;
  --line:#dddddd;
  --navy:#1f3c6e;
}
*{margin:0;padding:0;box-sizing:border-box}
html,body{width:1162px;height:1200px;overflow:hidden}
body{background:var(--bg-dark);position:relative;font-family:"Arimo",Arial,sans-serif;color:var(--text)}
.band-orange{position:absolute;left:0;top:141px;width:1162px;height:36px;background:var(--orange-band)}
.band-gray{position:absolute;left:0;top:177px;width:1162px;height:42px;background:var(--gray-band)}
.page{position:absolute;left:78px;top:0;width:996px;height:1200px;background:var(--page)}
.brand{position:absolute;left:12px;top:32px;display:flex;align-items:center;gap:14px}
.brand-mark{width:48px;height:48px;background:var(--orange)}
.brand-name{font-family:"Open Sans",sans-serif;font-weight:700;font-size:44px;color:var(--navy);line-height:1}
.brand-claim{position:absolute;left:188px;top:95px;font-family:"Open Sans",sans-serif;font-size:17px;color:var(--orange);font-weight:600}
.tools{position:absolute;right:20px;top:114px;display:flex;gap:13px}
.nav{position:absolute;left:6px;top:141px;width:981px;height:36px;background:var(--orange);display:flex;font-family:"Open Sans",sans-serif;font-size:14px;color:#fff;list-style:none}
.nav li{width:131px;line-height:36px;padding-left:28px;white-space:nowrap}
.nav li:first-child{width:102px;padding-left:24px}
.nav li.active{background:var(--nav-active);width:156px;padding-left:52px}
.banner{position:absolute;left:6px;top:180px;width:981px;height:276px;background:var(--banner);overflow:hidden}
.banner-shots{position:absolute;left:48px;top:40px;width:310px;height:190px;background:linear-gradient(180deg,#f4f4f4,#d9d9d9);border:1px solid #e8e8e8}
.starburst{position:absolute;left:300px;top:14px}
.banner-copy{position:absolute;left:388px;top:126px;color:#fff;font-family:"Arimo",Arial,sans-serif;text-shadow:0 1px 2px rgba(0,0,0,.4);white-space:nowrap}
.banner-copy .l1{font-size:21px}
.banner-copy .l1 b{font-size:19px}
.banner-copy .l2{font-size:28px;margin-left:190px}
.banner-name{position:absolute;right:60px;bottom:22px;font-family:"Open Sans",sans-serif;font-weight:700;font-size:30px;color:rgba(60,70,80,.45)}
.welcome{position:absolute;left:12px;top:468px;border-left:4px solid var(--orange);padding-left:8px}
.welcome h1{font-family:"Open Sans",sans-serif;font-size:16px;font-weight:700;color:#222}
.welcome p{font-family:"Open Sans",sans-serif;font-size:12px;color:var(--orange);margin-top:6px}
.intro{position:absolute;top:525px;width:300px;font-size:12px;line-height:17.5px;text-align:justify;color:#333}
.intro.c1{left:15px}.intro.c2{left:336px;width:290px}
.rating{position:absolute;left:734px;top:520px;width:250px;height:170px;background:linear-gradient(#f3f3f3,#dcdcdc);border-radius:8px;border:1px solid #ccc}
.rating .head{position:absolute;left:10px;top:10px;font-size:13px;color:#333}
.rating .head b{font-size:20px}
.rating .bubble{position:absolute;left:100px;top:68px;width:138px;height:62px;background:#fff;border-radius:8px}
.rating .more{position:absolute;right:18px;top:116px;font-size:9px;color:#5a8a2a;font-weight:700}
.rating .foot{position:absolute;left:18px;bottom:8px;font-size:12px;color:#333}
.rating .foot b{color:#4c8a1f}
.slogan{position:absolute;left:15px;top:696px;font-family:"Open Sans",sans-serif;font-size:19.5px;line-height:25px;color:var(--orange)}
.services{position:absolute;left:15px;top:768px;width:966px;display:flex}
.service{width:257px;height:100px;padding:6px 12px 0 48px;border-right:1px solid var(--line);position:relative}
.service:first-child{width:214px;padding-left:4px}
.service:last-child{border-right:none;width:238px}
.service h2{font-family:"Open Sans",sans-serif;font-size:12px;font-weight:600;color:#333;line-height:15px;white-space:nowrap}
.service p{font-family:"Open Sans",sans-serif;font-size:11px;color:var(--muted);line-height:14px;margin-top:9px;white-space:nowrap}
.service svg{position:absolute;right:24px;top:4px}
.footer-bar{position:absolute;left:6px;top:921px;width:981px;height:21px;background:var(--orange)}
.footer-notch{position:absolute;left:17px;top:942px}
.footer-nav{position:absolute;left:15px;top:958px;font-family:"Open Sans",sans-serif;font-size:11px;color:#333;word-spacing:3px}
.copyright{position:absolute;right:8px;top:958px;font-family:"Open Sans",sans-serif;font-size:11px;color:#333}
</style>
</head>
<body>
<div class="band-orange"></div>
<div class="band-gray"></div>
<div class="page">
  <div class="brand"><span class="brand-mark"></span><span class="brand-name">WEBHAUS</span></div>
  <div class="brand-claim">Wir halten Sie im Web</div>
  <div class="tools">
    <svg width="18" height="16" viewBox="0 0 18 16"><path d="M1 8 9 1l8 7M3 7v8h12V7" fill="none" stroke="#555" stroke-width="2"/></svg>
    <svg width="18" height="14" viewBox="0 0 18 14"><rect x="1" y="1" width="16" height="12" fill="none" stroke="#555" stroke-width="2"/><path d="M1 1l8 7 8-7" fill="none" stroke="#555" stroke-width="2"/></svg>
    <svg width="17" height="17" viewBox="0 0 17 17"><circle cx="7" cy="7" r="5" fill="none" stroke="#555" stroke-width="2"/><path d="M11 11l5 5" stroke="#555" stroke-width="3"/></svg>
  </div>
  <ul class="nav">
    <li>MENU 1</li><li class="active">MENU 2</li><li>MENU 3</li><li>MENU 4</li><li>MENU 5</li><li>MENU 6</li>
  </ul>
  <div class="banner">
    <div class="banner-shots" role="img" aria-label="Drei gestaffelte Bildschirmansichten der Webseite"></div>
    <svg class="starburst" width="120" height="120" viewBox="0 0 120 120">
      <polygon fill="#f47f20" stroke="#fff" stroke-width="2" points="60,4 68,20 85,10 87,29 106,27 99,45 116,54 101,66 112,82 93,85 95,104 77,98 69,115 60,100 51,115 43,98 25,104 27,85 8,82 19,66 4,54 21,45 14,27 33,29 35,10 52,20"/>
      <g fill="#fff" font-family="Open Sans,sans-serif" font-weight="700" font-size="13" text-anchor="middle" transform="rotate(-18 60 60)">
        <text x="60" y="48">JETZT</text><text x="60" y="64">KOSTENLOS</text><text x="60" y="80">TESTEN</text>
      </g>
    </svg>
    <div class="banner-copy">
      <div class="l1">Verwalten Sie Ihre Webseite - <b>einfach und unkompliziert</b></div>
      <div class="l2">Jetzt mit unseren <b>Editor</b></div>
    </div>
    <div class="banner-name">WEBHAUS</div>
  </div>
  <div class="welcome"><h1>Willkommen</h1><p>Bei Webhaus wir halten Sie im Web</p></div>
  <p class="intro c1">Heut zu Tage ist für Privatanwender sowie Unternehmen, eine effektive Webpräsentation mit besonderer Note unerlässlich. Sie suchen eine optimale Lösung? Dann sind Sie bei norvant design genau richtig? Wir sind bestrebt alles auf Ihre Wünsche ideal abzustimmen, dies erreichen wir durch barrierefreies und innovatives Webdesign. Da wir mit unseren Kunden eng zusammenarbeiten ist die Umsetzung um so leichter, da Probleme direkt beseitigt werden können.</p>
  <p class="intro c2">Um sich der Allgemeinheit perfekt darstellen zu können, ist das Internet genau der richtige Ort. Den es bietet das richtige Fundament für den Informationsfluss von Geschäftsabläufen und genau das zeichnet den Erfolg des Internets aus. Träumen Sie von einem Projekt im World Wide Web? Dann bieten wir Ihnen für Ihr Projekt ein individuell angepasstes Leistungspaket nach Ihren Vorstellungen an, um Ihre Webpräsentation erfolgreich hervorheben.</p>
  <div class="rating">
    <div class="head">Kundenbewertung <b>4.8</b> / 5</div>
    <svg style="position:absolute;left:8px;top:38px" width="160" height="28" viewBox="0 0 160 28">
      <g fill="#f5b400">
        <polygon id="s" points="14,1 17.5,10 27,10 19.5,16 22,26 14,20 6,26 8.5,16 1,10 10.5,10"/>
        <use href="#s" x="31"/><use href="#s" x="62"/><use href="#s" x="93"/><use href="#s" x="124"/>
      </g>
    </svg>
    <svg style="position:absolute;right:8px;top:4px" width="62" height="62"><circle cx="31" cy="31" r="29" fill="#e2a62a"/></svg>
    <svg style="position:absolute;left:14px;top:92px" width="70" height="40"><rect width="70" height="40" fill="#c9c9c9"/></svg>
    <div class="bubble"></div>
    <div class="more">MEHR...</div>
    <div class="foot"><b>GARANTIERT</b> echte Kundenmeinungen</div>
  </div>
  <div class="slogan">Ihre Lösung heißt Webhaus denn wir bringen Sie mit gutem Service an Ihr Ziel!<br>Unser Service für Sie;</div>
  <div class="services">
    <div class="service"><h2>SLABOPROUDÉ<br>SYSTÉMY</h2><p>krátný popisek o co<br>jde, co všechno firma<br>nabízí a co umí udělat</p>
      <svg width="54" height="54"><circle cx="27" cy="27" r="25" fill="#e0452b"/><path d="M15 39 39 15M15 15l24 24" stroke="#eee" stroke-width="5"/></svg></div>
    <div class="service"><h2>STRUKTUROVANÉ<br>A OPTICKÉ KABELÁŽE</h2><p>krátný popisek o co<br>jde, co všechno firma<br>nabízí a co umí udělat</p>
      <svg width="54" height="54"><circle cx="27" cy="27" r="25" fill="#f0b41e"/><rect x="10" y="14" width="32" height="24" rx="3" fill="#ddd" stroke="#666" stroke-width="2"/></svg></div>
    <div class="service"><h2>ICT PROJECT<br>MANAGEMENT</h2><p>krátný popisek o co<br>jde, co všechno firma<br>nabízí a co umí udělat</p>
      <svg width="54" height="54"><circle cx="27" cy="24" r="20" fill="#6bb33a"/><rect x="22" y="42" width="10" height="6" fill="#555"/><rect x="12" y="48" width="30" height="4" fill="#777"/></svg></div>
    <div class="service"><h2>INFORMAČNÍ<br>TECHNOLOGIE</h2><p>krátný popisek o co<br>jde, co všechno firma<br>nabízí a co umí udělat</p>
      <svg width="54" height="54"><circle cx="27" cy="27" r="25" fill="#3aa7d8"/><rect x="8" y="12" width="30" height="22" fill="#e8f4fa" stroke="#555" stroke-width="2"/><rect x="34" y="22" width="12" height="24" fill="#555"/></svg></div>
  </div>
  <div class="footer-bar"></div>
  <svg class="footer-notch" width="22" height="11"><polygon points="0,0 22,0 11,11" fill="#f47f20"/></svg>
  <div class="footer-nav">MENU 1 &nbsp;| &nbsp;MENU 2 &nbsp;| &nbsp;MENU 3 &nbsp;| &nbsp;MENU 4 &nbsp;| &nbsp;MENU 5 &nbsp;| &nbsp;MENU 6</div>
  <div class="copyright">COPYRIGHT @ WEBHAUS , ALL RIGHTS RESERVED 2009</div>
</div>
</body>
</html>
```